CloudRiver Business Card

I need something that flows with the logo and looks professional but creative. I included the thumbnail file of the photo but will upload the source file once I have it. Colors of business card should flow. I am interested in doing the translucent clear plastic cards as well. My company is called CloudRiver in one word and the contact details are below:

Dale Hollings
555-318-4720
www.CloudRiverTx.example
dhollings_47@mailbox.example
Updates

Too much red. I'd rather focus on the blue and put some silver or grey in there.

New Files uploaded. Like the designs so far and am looking forward to seeing more.

Looking for a whole new direction. Let's forget about the plastic card. Let's focus on the blue more than red. I still haven't seen something that really grabs me.

Industry/Entity Type

Plastic

```html
<!DOCTYPE html>
<html lang="en">
<head>
<meta charset="utf-8">
<title>CloudRiver Business Card</title>
<link href="https://fonts.googleapis.com/css2?family=Arimo:wght@400;700&display=swap" rel="stylesheet">
<style>
  :root {
    --backdrop: #e9e9ea;
    --card: #ffffff;
    --brand-silver: #a9afb6;
    --brand-silver-deep: #8b929a;
    --brand-blue: #1b77b3;
    --brand-blue-deep: #1d5f94;
    --ink: #2e2e2e;
    --ink-soft: #444444;
  }
  html, body {
    margin: 0;
    padding: 0;
    width: 1200px;
    height: 900px;
    overflow: hidden;
    background: var(--backdrop);
    font-family: "Arimo", Arial, sans-serif;
  }
  .sheet {
    position: relative;
    width: 1200px;
    height: 900px;
  }
  .card {
    position: absolute;
    left: 240px;
    width: 720px;
    height: 400px;
    background: var(--card);
    border-radius: 30px;
    overflow: hidden;
    box-shadow: 0 6px 18px rgba(0,0,0,0.18);
  }
  .card--back { top: 35px; }
  .card--front { top: 465px; }

  .wordmark {
    font-family: "Arimo", Arial, sans-serif;
    font-weight: 400;
    color: var(--brand-blue-deep);
    letter-spacing: 0.5px;
    white-space: nowrap;
  }
  .card--back .wordmark {
    position: absolute;
    left: 0;
    right: 0;
    top: 160px;
    text-align: center;
    font-size: 64px;
  }
  .card--front .wordmark {
    position: absolute;
    left: 470px;
    top: 150px;
    font-size: 44px;
  }

  .side-band {
    position: absolute;
    left: 0;
    top: 0;
    width: 140px;
    height: 400px;
  }
  .band-silver { fill: var(--brand-silver); }
  .band-blue { fill: var(--brand-blue); }

  .identity {
    position: absolute;
    left: 175px;
    top: 110px;
  }
  .identity__name {
    margin: 0;
    font-size: 28px;
    font-weight: 700;
    color: var(--brand-blue-deep);
  }
  .identity__role {
    margin: 6px 0 0 -6px;
    font-size: 22px;
    color: var(--ink);
  }

  .contacts {
    position: absolute;
    left: 150px;
    top: 235px;
    margin: 0;
    padding: 0;
    list-style: none;
    font-size: 17px;
    color: var(--ink-soft);
  }
  .contacts li {
    display: flex;
    align-items: center;
    gap: 9px;
    height: 26px;
    white-space: nowrap;
  }
  .contacts svg {
    width: 17px;
    height: 17px;
    flex: none;
  }
  .icon-stroke { fill: none; stroke: var(--brand-silver-deep); stroke-width: 2; }
  .icon-fill { fill: var(--brand-silver-deep); }
  .icon-social { fill: var(--brand-blue); }
</style>
</head>
<body>
<main class="sheet">

  <section class="card card--back" aria-label="Card back">
    <div class="wordmark">CloudRiver</div>
  </section>

  <section class="card card--front" aria-label="Card front">
    <svg class="side-band" viewBox="0 0 140 400" aria-hidden="true">
      <path class="band-silver" d="M0 0 H70 C38 110 34 260 100 400 H0 Z"/>
      <path class="band-blue" d="M70 0 H118 C74 100 70 250 104 400 H100 C34 260 38 110 70 0 Z"/>
    </svg>

    <div class="identity">
      <h1 class="identity__name">Dale Hollings</h1>
      <p class="identity__role">Founder</p>
    </div>

    <ul class="contacts">
      <li style="margin-left:22px">
        <svg viewBox="0 0 16 16" aria-hidden="true"><rect class="icon-stroke" x="4" y="1" width="8" height="14" rx="1.5"/><rect class="icon-fill" x="7" y="12" width="2" height="1.5"/></svg>
        555-318-4720
      </li>
      <li style="margin-left:14px">
        <svg viewBox="0 0 16 16" aria-hidden="true"><rect class="icon-fill" x="1" y="3" width="14" height="10" rx="1"/><path d="M1.5 4 L8 9 L14.5 4" fill="none" stroke="#fff" stroke-width="1.4"/></svg>
        dhollings_47@mailbox.example
      </li>
      <li style="margin-left:7px">
        <svg viewBox="0 0 16 16" aria-hidden="true"><circle class="icon-stroke" cx="8" cy="8" r="6.5" stroke-width="1.5"/><ellipse class="icon-stroke" cx="8" cy="8" rx="3" ry="6.5" stroke-width="1.2"/><path class="icon-stroke" d="M1.5 8 H14.5 M2.5 4.8 H13.5 M2.5 11.2 H13.5" stroke-width="1.1"/></svg>
        www.CloudRiverTx.example
      </li>
      <li>
        <svg viewBox="0 0 16 16" aria-hidden="true"><circle class="icon-social" cx="8" cy="8" r="7"/></svg>
        @cloudriver
      </li>
    </ul>

    <div class="wordmark">CloudRiver</div>
  </section>

</main>
</body>
</html>
```